Presentation Folder - Stagger Cut Fliers
Keystone Realty Group
Presentation Folder - Stagger Cut Fliers - Real Estate
Creative Brief
Real Estate
Corporate. Our target audience are real estate agents and brokers. This is an industry where image and perception matter, so these designs need to invoke professionalism, be creative, and invoke confidence in our services.
The presentation folder itself needs to be very simple, but again, very professional and aesthetically pleasing. At a minimum, we need our logo on the font and the company contact information on the back. The stagger cut fliers themselves need to have the ability to put information on the front and back of the flier. There are five pages for the fliers, so you can either design five unique pages or have a template that can work for all of them. You can use filler text like that in the attached document. The fliers aren't just going to be text. You can add filler images to make more appealing, such as on the consumer demand page you can leave a spot where we can put the image of a billboard.

```html
<!DOCTYPE html>
<html lang="en">
<head>
<meta charset="utf-8">
<title>Keystone Realty Group – Presentation Folder</title>
<link href="https://fonts.googleapis.com/css2?family=Open+Sans:wght@400;600;700&display=swap" rel="stylesheet">
<style>
  :root {
    --stage: #cfd1d3;
    --paper: #ffffff;
    --blue-deep: #0d5fa8;
    --blue-mid: #2b86d0;
    --blue-light: #6fb9ec;
    --brand-navy: #1b4f8a;
    --ink-soft: #6d737a;
    --rule: #e4e6e8;
  }
  * { margin: 0; padding: 0; box-sizing: border-box; }
  html, body { width: 1200px; height: 1080px; overflow: hidden; background: var(--stage); }
  body { font-family: "Open Sans", Arial, sans-serif; position: relative; }
  .folder-art { position: absolute; inset: 0; }

  .brand {
    position: absolute; display: flex; align-items: center;
    color: var(--brand-navy); font-weight: 600; white-space: nowrap;
  }
  .brand-dot { border-radius: 50%; background: var(--blue-mid); flex: none; }
  .brand--cover { left: 700px; top: 340px; font-size: 30px; gap: 14px; letter-spacing: -0.3px; }
  .brand--cover .brand-dot { width: 64px; height: 64px; }
  .brand--back { left: 100px; top: 670px; font-size: 14px; gap: 7px; }
  .brand--back .brand-dot { width: 28px; height: 28px; }

  .contact {
    position: absolute; left: 372px; top: 666px;
    font-size: 9.5px; line-height: 13px; color: var(--ink-soft);
  }
  .contact span { display: inline-block; min-width: 130px; }

  .pocket-url {
    position: absolute; font-size: 11px; color: rgba(255,255,255,0.85);
    transform: rotate(180deg); white-space: nowrap;
  }
  .pocket-url--left { left: 120px; top: 782px; }
  .pocket-url--right { left: 905px; top: 782px; }
</style>
</head>
<body>
  <svg class="folder-art" width="1200" height="1080" viewBox="0 0 1200 1080" aria-hidden="true">
    <defs>
      <linearGradient id="bandFill" x1="0" y1="0" x2="1" y2="0">
        <stop offset="0" stop-color="#0d5fa8"/>
        <stop offset="0.55" stop-color="#6fb9ec"/>
        <stop offset="1" stop-color="#0d5fa8"/>
      </linearGradient>
      <linearGradient id="pocketFill" x1="0" y1="0" x2="0" y2="1">
        <stop offset="0" stop-color="#6fb9ec"/>
        <stop offset="0.45" stop-color="#2b86d0"/>
        <stop offset="1" stop-color="#0d5fa8"/>
      </linearGradient>
      <radialGradient id="glow" cx="0.5" cy="1" r="0.8">
        <stop offset="0" stop-color="#eef3f7"/>
        <stop offset="1" stop-color="#ffffff" stop-opacity="0"/>
      </radialGradient>
    </defs>

    <!-- cover sheet -->
    <rect class="sheet" x="62" y="52" width="1076" height="694" fill="#ffffff"/>
    <rect class="top-band" x="62" y="52" width="1076" height="18" fill="url(#bandFill)"/>
    <rect x="62" y="70" width="1076" height="676" fill="url(#glow)" role="img" aria-label="Soft light rays background"/>
    <line class="fold" x1="640" y1="70" x2="640" y2="746" stroke="#e4e6e8" stroke-width="1.5"/>
    <rect x="62" y="740" width="1076" height="6" fill="#2b86d0" opacity="0.35"/>

    <!-- stagger cut pockets -->
    <path class="pocket pocket--left" d="M62 754 H640 V1007 H62 Z" fill="url(#pocketFill)"/>
    <path class="pocket pocket--right" d="M650 754 Q660 860 690 870 H1138 V754 Z M650 754 V1007 H1138 V754 Z" fill="url(#pocketFill)"/>
    <path d="M62 930 Q350 860 640 905 V1007 H62 Z" fill="#0d5fa8" opacity="0.35"/>
    <path d="M650 930 Q900 860 1138 905 V1007 H650 Z" fill="#0d5fa8" opacity="0.35"/>
    <path d="M62 900 Q350 830 640 880" stroke="#ffffff" stroke-opacity="0.25" stroke-width="3" fill="none"/>
    <path d="M650 900 Q900 830 1138 880" stroke="#ffffff" stroke-opacity="0.25" stroke-width="3" fill="none"/>
    <line x1="645" y1="754" x2="645" y2="1007" stroke="#cfd1d3" stroke-width="8"/>

    <circle class="pocket-mark" cx="158" cy="862" r="32" fill="#ffffff"/>
    <circle class="pocket-mark" cx="1090" cy="862" r="32" fill="#ffffff"/>
  </svg>

  <div class="brand brand--cover"><span class="brand-dot"></span>Keystone Realty Group</div>

  <div class="brand brand--back"><span class="brand-dot"></span>Keystone Realty Group</div>
  <div class="contact">
    2140 Harbor Ln., Ste. 6 &nbsp; Cedar Park, Texas 78613<br>
    <span>Phone: (512) 555-0148</span>Fax: (512) 555-0192<br>
    Toll Free: (800) 555-0176
  </div>

  <div class="pocket-url pocket-url--left">www.keystonerealtygroup.com</div>
  <div class="pocket-url pocket-url--right">www.keystonerealtygroup.com</div>
</body>
</html>
```